Detail Shop Business card design

i need a business card design for my new detailing company called 'Brenner's Detail Shop'. i want an all black and white design . simple, direct and to the point. i want the designer to choose a fitting font to match the logothe front should have logo, address, phone and email and the back side should have a slogan and text indicating that we offer services on anything including cars, trucks, motorcycles and RVs. slogan will read "we take pride in your ride"
maybe also very small on the back side the IG icon with Brenners_Detail_Shop

phone 482.615.7734
address 7384 E Harlow Ave
Spokane WA 99342
email: BrennersDetail@quorvail.com

Target Market(s)

all ages , auto enthusiasts

Industry/Entity Type

Automotive

Contact Information for Business Card

the front should have logo, address, phone and email and the back side should have a slogan and text indicating that we offer services on anything including cars, trucks, motorcycles and RVs. slogan will read "we take pride in your ride"

phone 482.615.7734
address 7384 E Harlow Ave
Spokane WA 99342

Colors
000000
ffffff

Requirements
Must have
• bold font and very simple design with good spacing
Nice to have
• anything creative from the designer indicating we service any types of vehicles
Should not have
• any colors ,

```html
<!DOCTYPE html>
<html lang="en">
<head>
<meta charset="utf-8">
<title>Brenner's Detail Shop – Business Card</title>
<link rel="stylesheet" href="https://fonts.googleapis.com/css2?family=Open+Sans:wght@400;600;700&display=swap">
<style>
  :root {
    --bg: #3a322e;
    --card: #141414;
    --card-edge: #1e1e1e;
    --ink: #ffffff;
    --ink-soft: #d8d8d8;
    --art-light: #8a8a8a;
    --art-dark: #2a2a2a;
  }
  * { box-sizing: border-box; margin: 0; padding: 0; }
  html, body { width: 1200px; height: 864px; overflow: hidden; }
  body {
    background: var(--bg);
    font-family: "Open Sans", Arial, sans-serif;
    color: var(--ink);
    position: relative;
  }
  .card {
    position: absolute;
    width: 540px;
    height: 310px;
    background: var(--card);
    border: 1px solid var(--card-edge);
    box-shadow: 0 10px 24px rgba(0,0,0,.45);
  }
  /* Back side */
  .card-back { left: 40px; top: 277px; }
  .vehicle-art {
    position: absolute;
    left: 130px; top: 34px;
    width: 240px; height: 130px;
    border-radius: 50% 50% 8px 8px / 40% 40% 8px 8px;
    background: radial-gradient(ellipse at 40% 45%, var(--art-light), var(--art-dark) 75%);
  }
  .slogan {
    position: absolute;
    left: 60px; top: 178px; width: 400px;
    text-align: center;
    font-weight: 700;
    font-size: 17px;
    letter-spacing: .5px;
    text-transform: uppercase;
  }
  .slogan-rule {
    position: absolute;
    left: 60px; top: 206px; width: 400px;
    border-top: 1.5px solid var(--ink);
  }
  .services {
    position: absolute;
    left: 30px; top: 216px; width: 460px;
    text-align: center;
    font-size: 13px;
    color: var(--ink-soft);
  }
  /* Front side */
  .card-front { left: 620px; top: 277px; }
  .person {
    position: absolute; left: 32px; top: 40px;
  }
  .person-name { font-weight: 700; font-size: 17px; text-transform: uppercase; }
  .person-title { font-size: 12px; text-transform: uppercase; color: var(--ink-soft); }
  .contacts {
    position: absolute; left: 32px; top: 90px;
    list-style: none;
    font-size: 13px;
    line-height: 19px;
  }
  .contacts li { display: flex; align-items: center; gap: 8px; }
  .contacts svg { width: 11px; height: 11px; fill: var(--ink); flex: none; }
  .rule {
    position: absolute; left: 32px; width: 476px;
    border-top: 1.5px solid var(--ink);
  }
  .rule-top { top: 190px; }
  .rule-bottom { top: 246px; }
  .brand {
    position: absolute; right: 28px; top: 110px;
    display: flex; align-items: center; gap: 8px;
    width: 170px;
  }
  .brand-dot {
    width: 16px; height: 16px; border-radius: 50%;
    background: var(--ink); flex: none;
  }
  .brand-name {
    font-weight: 700; font-size: 15px; line-height: 18px;
    text-transform: uppercase;
  }
  .address {
    position: absolute; right: 32px; top: 256px;
    text-align: right; font-size: 13px; line-height: 18px;
  }
</style>
</head>
<body>
  <section class="card card-back" aria-label="Card back">
    <div class="vehicle-art" role="img" aria-label="Silver hot rod car illustration"></div>
    <p class="slogan">We take pride in your ride</p>
    <div class="slogan-rule"></div>
    <p class="services">we offer services on anything including cars, trucks, motorcycles &amp; RVs</p>
  </section>

  <section class="card card-front" aria-label="Card front">
    <div class="person">
      <p class="person-name">Marcus Hale</p>
      <p class="person-title">President</p>
    </div>
    <ul class="contacts">
      <li><svg viewBox="0 0 12 12"><path d="M2 1h2.5l1 3-1.5 1a7 7 0 0 0 3 3l1-1.5 3 1V10a1 1 0 0 1-1 1A9 9 0 0 1 1 2a1 1 0 0 1 1-1z"/></svg>482.615.7734</li>
      <li><svg viewBox="0 0 12 12"><path d="M3.5 0h5a1 1 0 0 1 1 1v10a1 1 0 0 1-1 1h-5a1 1 0 0 1-1-1V1a1 1 0 0 1 1-1zm0 1.5v8h5v-8z"/></svg>714 205 8831</li>
      <li><svg viewBox="0 0 12 12"><path d="M0 2h12v8H0zm1 1v.4l5 3.2 5-3.2V3z"/></svg>BrennersDetail@quorvail.com</li>
      <li><svg viewBox="0 0 12 12"><circle cx="6" cy="6" r="6"/></svg>www.brennersdetail.com</li>
    </ul>
    <div class="rule rule-top"></div>
    <div class="brand">
      <span class="brand-dot"></span>
      <span class="brand-name">Brenner's Detail Shop</span>
    </div>
    <div class="rule rule-bottom"></div>
    <p class="address">7384 E Harlow Ave<br>Spokane WA 99342</p>
  </section>
</body>
</html>
```